Corvella Web Design Project

I am attaching my logo so I need to see applied to the website developed by you guys!!
Tbahks!!
Ferruccio
This is the DNA of the company
Flat and dynamic organization - Informal and respectful social approac
Innovative - Always striving for the best solution
Reliability and Quality - The value of our name
Flexibility - Ability to handle new requirements and unforeseen events
Simplicity - Technology must serve – NOT rule!
Cooperative Relations - The synergy that makes 1+1=3
We still don´t have our logo as we have another open project on artbazaarly
Our company won´t be selling this equipment but providing welding services for shipyard industry, as you can see on the website below.
www.velmorasystems.example
Reason: Hi webdesigners,
I will be deciding my logo by this weekend as soon as I have decided I will post my logo to see it applied to your design!!!
Thanks
Ferruccio
I just Sent my logo for your attention!!!!
Welding

```html
<!DOCTYPE html>
<html lang="en">
<head>
<meta charset="utf-8">
<title>Corvella – Robotic Welding Technologie</title>
<link href="https://fonts.googleapis.com/css2?family=Oswald:wght@300;400&family=Open+Sans:wght@400;600;700&display=swap" rel="stylesheet">
<style>
:root{
  --orange:#f15a24;
  --orange-deep:#d9481a;
  --ink:#333;
  --muted:#555;
  --white:#fff;
  --charcoal:#252323;
  --card-line:#8a8685;
  --footer:#111;
}
*{box-sizing:border-box;margin:0;padding:0}
html,body{width:1200px;height:2744px;overflow:hidden}
body{font-family:"Open Sans",Arial,sans-serif;color:var(--ink);background:var(--white);position:relative}
.wrap{position:relative;width:836px;margin:0 auto;height:100%}
section,header,footer{position:relative;width:1200px;overflow:hidden}

/* header */
.site-header{height:77px;background:var(--white)}
.brand{position:absolute;left:0;top:12px;display:flex;align-items:center;gap:8px}
.brand-dot{width:44px;height:44px;border-radius:50%;background:var(--orange)}
.brand-name{font-family:"Open Sans",sans-serif;font-weight:400;font-size:40px;line-height:40px;color:#3a3a3a}
.brand-tag{position:absolute;left:52px;top:52px;font-size:9px;letter-spacing:1px;color:#777;white-space:nowrap}
.main-nav{position:absolute;right:0;top:30px;display:flex;gap:22px;align-items:center;font-family:"Oswald",sans-serif;font-size:14px;color:#333}
.main-nav .active{color:var(--orange)}

/* hero */
.hero{height:413px;background:linear-gradient(100deg,#1e2c52 0%,#8a3a14 30%,#e2661f 45%,#3a3a48 65%,#b04a18 85%,#1c2440 100%)}
.hero-photo{position:absolute;inset:0}
.hero-title{position:absolute;top:95px;left:0;width:1200px;text-align:center;font-family:"Oswald",sans-serif;font-weight:400;font-size:58px;line-height:60px;color:var(--orange)}
.hero-sub{position:absolute;top:150px;left:0;width:1200px;text-align:center;font-family:"Oswald",sans-serif;font-weight:300;font-size:40px;line-height:46px;color:var(--white)}
.hero-thumbs{position:absolute;left:183px;top:313px;display:flex;gap:17px}
.thumb{width:196px;height:100px;border-top:5px solid var(--orange);background:linear-gradient(135deg,#31405e,#c8622a 60%,#2b3352)}
.thumb.raised{margin-top:-28px;height:128px}

/* intro */
.intro{height:282px}
.intro .wrap{display:flex;gap:24px;padding-top:45px}
.intro-col{width:406px}
.intro h2{font-family:"Oswald",sans-serif;font-weight:300;font-size:22px;color:var(--orange);margin-bottom:14px}
.intro h2 span{color:#333}
.intro p{font-size:10px;line-height:17px;color:var(--muted);margin-bottom:17px}

/* products */
.products{height:461px;background:linear-gradient(180deg,#e8602a,#ef7038 50%,#e35a22)}
.products h2{text-align:center;font-family:"Oswald",sans-serif;font-weight:300;font-size:24px;color:var(--white);padding-top:30px}
.product-row{position:absolute;top:80px;left:181px;display:flex;gap:21px}
.product{width:265px}
.product-photo{height:145px;border:2px solid var(--white)}
.product h3{font-family:"Oswald",sans-serif;font-weight:300;font-size:17px;color:var(--white);margin:18px 0 22px}
.product p{font-size:10px;line-height:17px;color:var(--white);height:80px}
.pill{display:inline-block;background:var(--white);color:#222;font-family:"Oswald",sans-serif;font-size:10px;letter-spacing:.5px;border-radius:10px;padding:3px 0;width:100px;text-align:center}
.more-tab{position:absolute;left:545px;bottom:0;width:118px;height:22px;background:var(--white);border-radius:14px 14px 0 0;text-align:center;font-family:"Oswald",sans-serif;font-size:10px;line-height:24px;color:#222}

/* services */
.services{height:463px;background:var(--charcoal)}
.service-row{position:absolute;top:77px;left:243px;display:flex;gap:20px}
.service{width:225px}
.service-bar{height:7px;background:var(--orange);margin-bottom:7px}
.service-box{height:298px;border:1px solid var(--card-line);text-align:center;color:var(--white);padding-top:20px}
.service-box svg{width:56px;height:56px}
.service h3{font-family:"Oswald",sans-serif;font-weight:300;font-size:17px;line-height:24px;color:var(--orange);margin:16px 0 18px}
.service p{font-size:10px;line-height:18px;padding:0 14px;height:108px;margin-bottom:10px}
.service .btn{display:inline-block;width:102px;padding:3px 0;border-radius:10px;background:var(--orange);font-family:"Oswald",sans-serif;font-size:10px;color:var(--white)}
.service .btn.light{background:var(--white);color:#222}
.service.dim .service-box{background:#2f2c2c}

/* contact */
.contact{height:623px;background:linear-gradient(180deg,#2a2a2c 0%,#3a3b3d 45%,#2c2a28 100%);font-family:Arial,Helvetica,sans-serif;color:var(--white)}
.contact h2{text-align:center;font-size:28px;font-weight:700;padding-top:40px}
.contact .lead{text-align:center;font-size:12px;margin-top:14px}
.field-row{position:absolute;top:148px;left:183px;display:flex;gap:16px}
.field{width:268px;height:40px;border:1px solid #cfcfcf;display:flex;align-items:center;gap:10px;padding-left:14px;font-size:12px}
.field svg{width:14px;height:14px;fill:var(--white)}
.message{position:absolute;top:203px;left:183px;width:836px;height:148px;border:1px solid #cfcfcf;padding:14px;display:flex;gap:10px;font-size:12px}
.message svg{width:18px;height:16px}
.submit{position:absolute;top:365px;left:183px;width:836px;height:33px;background:var(--orange);text-align:center;line-height:33px;font-size:12px;font-weight:700;letter-spacing:.5px}
.rule{position:absolute;left:183px;width:836px;height:2px;display:flex;gap:8px}
.rule i{flex:1;background:#ddd}
.info{position:absolute;top:455px;left:183px;width:836px;display:flex;text-align:center}
.info div{flex:1}
.info .label{color:var(--orange)}
.physical{padding:0 14px}
.physical .label{font-size:17px}
.physical p{font-size:17px;line-height:22px;margin-top:2px}
.emails{font-size:12px;line-height:16px}
.phones{font-size:17px;line-height:22px;padding-top:16px}

/* map */
.map{height:373px;background:linear-gradient(135deg,#e6e3dc,#dedad2 50%,#e9e6df)}

.site-footer{height:52px;background:var(--footer);color:var(--white);font-size:10px}
.site-footer p{position:absolute;left:183px;top:20px}
</style>
</head>
<body>

<header class="site-header">
  <div class="wrap">
    <div class="brand">
      <span class="brand-dot"></span>
      <span class="brand-name">Corvella</span>
    </div>
    <span class="brand-tag">ROBOTIC WELDING TECHNOLOGIE</span>
    <nav class="main-nav">
      <span class="active">Home</span><span>About us</span><span>Competence</span><span>Case Story</span><span>Products</span><span>Videos</span>
      <svg width="16" height="16" viewBox="0 0 16 16"><circle cx="9.5" cy="6.5" r="5" fill="none" stroke="#f15a24" stroke-width="2"/><line x1="6" y1="10" x2="1.5" y2="14.5" stroke="#f15a24" stroke-width="2.4"/></svg>
    </nav>
  </div>
</header>

<section class="hero">
  <div class="hero-photo" role="img" aria-label="Robotic welding arm in a workshop throwing bright sparks"></div>
  <h1 class="hero-title">CORVELLA</h1>
  <p class="hero-sub">ENGINEERING &amp; CONSTRCTION</p>
  <div class="hero-thumbs">
    <div class="thumb" role="img" aria-label="Welding robot at work"></div>
    <div class="thumb" role="img" aria-label="Orange robot arm on a production line"></div>
    <div class="thumb raised" role="img" aria-label="Welding torch with sparks"></div>
    <div class="thumb" role="img" aria-label="Close-up of a welding seam with sparks"></div>
  </div>
</section>

<section class="intro">
  <div class="wrap">
    <div class="intro-col">
      <h2>WELCOME TO <span>CORVELLA.</span></h2>
      <p>Lorem Ipsum is simply dummy text of the printing and typesetting industry. Lorem Ipsum has been the industry's standard dummy text ever since the 1500s, when an unknown printer took a galley of type and scrambled it to make a type specimen book.</p>
      <p>Lorem Ipsum is simply dummy text of the printing and typesetting industry. Lorem Ipsum has been the industry's standard dummy text ever since the 1500s, when an unknown printer took a galley of type and scrambled it to make a type specimen book.Lorem Ipsum is simply dummy text of the printing and typesetting industry. Lorem Ipsum has been the industry's standard dummy text ever since the 1500s.</p>
    </div>
    <div class="intro-col">
      <h2>ABOUT US</h2>
      <p>Lorem Ipsum is simply dummy text of the printing and typesetting industry. Lorem Ipsum has been the industry's standard dummy text ever since the 1500s, when an unknown printer took a galley of type and scrambled it to make a type specimen book.</p>
      <p>It has survived not only five centuries, but also the leap into electronic typesetting, remaining essentially unchanged. It was popularised in the 1960s with the release of Sheetmark sheets containing Lorem Ipsum passages, and more recently with desktop publishing software like Pagewright Studio including versions of Lorem Ipsum. publishing software like Pagewright Studio including versions of Lorem Ipsum.</p>
    </div>
  </div>
</section>

<section class="products" role="region" aria-label="Our products">
  <h2>OUR PRODUCTS</h2>
  <div class="product-row">
    <div class="product">
      <div class="product-photo" style="background:linear-gradient(180deg,#fff,#f2eeea)" role="img" aria-label="Orange industrial robot arm"></div>
      <h3>GENERAL FEATURES</h3>
      <p>Lorem Ipsum has been the industry's standard dummy text ever since the 1500s, when an unknown printer took a galley of type and scrambled it to make a type specimen book.</p>
      <span class="pill">LEARN MORE</span>
    </div>
    <div class="product">
      <div class="product-photo" style="background:linear-gradient(160deg,#e4e4e2,#c9ca9a 55%,#8e8e8a)" role="img" aria-label="Mini crawler welding robot on a track"></div>
      <h3>MINI CRAWLER WELDING ROBOT</h3>
      <p>Lorem Ipsum has been the industry's standard dummy text ever since the 1500s, when an unknown printer took a galley of type and scrambled it to make a type specimen book.</p>
      <span class="pill">LEARN MORE</span>
    </div>
    <div class="product">
      <div class="product-photo" style="background:linear-gradient(160deg,#5a6275,#8a7a78 50%,#c7c9d8)" role="img" aria-label="Gantry welding robot in a hall"></div>
      <h3>GANTRY WELDING ROBOT</h3>
      <p>Lorem Ipsum has been the industry's standard dummy text ever since the 1500s, when an unknown printer took a galley of type and scrambled it to make a type specimen book.</p>
      <span class="pill">LEARN MORE</span>
    </div>
  </div>
  <div class="more-tab">MORE PRODUCTS</div>
</section>

<section class="services">
  <div class="service-row">
    <div class="service dim">
      <div class="service-bar"></div>
      <div class="service-box">
        <svg viewBox="0 0 56 56" fill="#fff"><path d="M6 10h32a4 4 0 0 1 4 4v18a4 4 0 0 1-4 4H20l-9 8v-8H6a4 4 0 0 1-4-4V14a4 4 0 0 1 4-4z"/><path d="M46 20h4a4 4 0 0 1 4 4v16a4 4 0 0 1-4 4h-3v7l-8-7H28a4 4 0 0 1-4-4v-2h16a6 6 0 0 0 6-6z"/></svg>
        <h3>WHAT OUR CLIENT SAY</h3>
        <p>Lorem Ipsum has been the industry's standard dummy text ever since the 1500s, when an unknown printer took a galley of type and scrambled it to make a type specimen book.</p>
        <span class="btn light">LEARN MORE</span>
      </div>
    </div>
    <div class="service">
      <div class="service-bar"></div>
      <div class="service-box">
        <svg viewBox="0 0 56 56"><rect x="4" y="10" width="48" height="42" rx="3" fill="none" stroke="#fff" stroke-width="3"/><rect x="4" y="10" width="48" height="10" fill="#fff"/><rect x="14" y="4" width="4" height="10" fill="#fff"/><rect x="38" y="4" width="4" height="10" fill="#fff"/><g fill="#fff"><rect x="10" y="25" width="6" height="5"/><rect x="20" y="25" width="6" height="5"/><rect x="30" y="25" width="6" height="5"/><rect x="40" y="25" width="6" height="5"/><rect x="10" y="34" width="6" height="5"/><rect x="20" y="34" width="6" height="5"/><rect x="30" y="34" width="6" height="5"/><rect x="40" y="34" width="6" height="5"/><rect x="10" y="43" width="6" height="5"/><rect x="20" y="43" width="6" height="5"/><rect x="30" y="43" width="6" height="5"/></g></svg>
        <h3>REQUEST FREE ESTIMATE</h3>
        <p>Lorem Ipsum has been the industry's standard dummy text ever since the 1500s, when an unknown printer took a galley of type and scrambled it to make a type specimen book.</p>
        <span class="btn">LEARN MORE</span>
      </div>
    </div>
    <div class="service">
      <div class="service-bar"></div>
      <div class="service-box">
        <svg viewBox="0 0 56 56" fill="#fff"><path d="M4 14l14-5 14 5 14-5v38l-14 5-14-5-14 5z" fill="none" stroke="#fff" stroke-width="3" stroke-linejoin="round"/><line x1="18" y1="9" x2="18" y2="47" stroke="#fff" stroke-width="3"/><line x1="32" y1="14" x2="32" y2="52" stroke="#fff" stroke-width="3"/><path d="M44 2a7 7 0 0 1 7 7c0 5-7 13-7 13s-7-8-7-13a7 7 0 0 1 7-7z"/><circle cx="44" cy="9" r="2.5" fill="#252323"/></svg>
        <h3>REQUEST BROCHURE</h3>
        <p>Lorem Ipsum has been the industry's standard dummy text ever since the 1500s, when an unknown printer took a galley of type and scrambled it to make a type specimen book.</p>
        <span class="btn">LEARN MORE</span>
      </div>
    </div>
  </div>
</section>

<section class="contact" role="img" aria-label="Dim photo of a modern kitchen interior behind the contact form">
  <h2>CONTACT</h2>
  <p class="lead">Feel free to fill out the form below to schedule a Project Request, we promise to get back to you within a 24 hour period.</p>
  <div class="field-row">
    <div class="field"><svg viewBox="0 0 14 14"><circle cx="7" cy="4" r="3.3"/><path d="M0 14c0-4 3-6 7-6s7 2 7 6z"/></svg>Your Name</div>
    <div class="field"><svg viewBox="0 0 14 14"><path d="M3 0l3 3-2 2c1 2 3 4 5 5l2-2 3 3-2 3C6 14 0 8 0 3z"/></svg>Your Phone</div>
    <div class="field"><svg viewBox="0 0 14 14"><rect x="0.7" y="2.7" width="12.6" height="8.6" fill="none" stroke="#fff" stroke-width="1.4"/><path d="M1 3l6 5 6-5" fill="none" stroke="#fff" stroke-width="1.4"/></svg>Your Email</div>
  </div>
  <div class="message"><svg viewBox="0 0 18 16"><rect x="5" y="1" width="12" height="9" rx="2" fill="none" stroke="#fff" stroke-width="1.4"/><rect x="1" y="5" width="11" height="8" rx="2" fill="#fff"/><path d="M3 13v3l3-3z" fill="#fff"/></svg>Describe Your Project</div>
  <div class="submit">SUBMIT</div>
  <div class="rule" style="top:439px"><i></i><i></i><i></i></div>
  <div class="info">
    <div class="physical"><span class="label">Physical</span><p>Lorem Ipsum has been the industry's standard dummy text ever since.</p></div>
    <div class="emails"><span class="label">Accounting:</span><br>info@corvella.example<br><span class="label">DNS Requests:</span><br>dnsmanagement@corvella.example<br><span class="label">Support:</span><br>help@corvella.example</div>
    <div class="phones"><span class="label">Toll Free:</span> (000) 000-0000<br><span class="label">Local:</span> (000) 000-0000</div>
  </div>
  <div class="rule" style="top:573px"><i></i><i></i><i></i></div>
</section>

<section class="map" role="img" aria-label="Street map showing the office location with a red pin"></section>

<footer class="site-footer"><p>© 2014 Corvella.</p></footer>

</body>
</html>
```